Standard logo business card

We are seeking a solid, somewhat understated professional design. We are a tech company. We like fonts similar to Aptifer Slab. Front side will be white with the contact information and a small version of our primary (Light background) logo.

(We have three people so we will have three names and titles)

Back side will hold our reverse logo on dark background along with the tagline:

"Intelligent annotation solutions for complex data"

Target Market(s)

Professionals, Tech

Industry/Entity Type

Business

Contact Information for Business Card

Name
Title

Phone
Email
City, State
Website

[We will email leading designer specific contact information)

Font styles to use
Serif

Requirements
Must have
• Colors are:
• Orange RGB 245,92,23
• Blue RGB 3,34,56
Nice to have
• We like a split with the Name and Title on the right and then contact details (below) on the left.

```html
<!DOCTYPE html>
<html lang="en">
<head>
<meta charset="utf-8">
<title>Corvana business card</title>
<link rel="stylesheet" href="https://fonts.googleapis.com/css2?family=Tinos:wght@400;700&display=swap">
<style>
  :root {
    --orange: rgb(245, 92, 23);
    --navy: rgb(3, 34, 56);
    --navy-edge: #22384c;
    --paper: #f7f7f6;
    --backdrop: #e6e4e1;
    --serif: "Tinos", "Times New Roman", serif;
  }
  * { box-sizing: border-box; margin: 0; padding: 0; }
  html, body { width: 1200px; height: 1037px; overflow: hidden; }
  body {
    background: var(--backdrop);
    font-family: var(--serif);
    position: relative;
  }
  .card {
    position: absolute;
    left: 260px;
    width: 680px;
    height: 388px;
    background: var(--paper);
    box-shadow: 0 6px 18px rgba(0,0,0,0.18);
    overflow: hidden;
  }
  .card--contact { top: 70px; }
  .card--brand { top: 560px; }

  /* contact side */
  .edge-band {
    position: absolute; left: 0; top: 0; bottom: 0; width: 26px;
    background: var(--navy-edge);
  }
  .brand-column {
    position: absolute; left: 26px; top: 0; bottom: 0; width: 234px;
    display: flex; flex-direction: column; align-items: center; justify-content: center;
    gap: 8px;
  }
  .info-panel {
    position: absolute; left: 260px; right: 0; top: 0; bottom: 0;
    background: var(--navy);
    color: #fff;
  }
  .person { position: absolute; left: 46px; top: 40px; }
  .person__name { font-size: 27px; letter-spacing: 0.5px; }
  .person__title { font-size: 14px; margin-top: 2px; }
  .contact-list {
    position: absolute; left: 40px; bottom: 56px;
    list-style: none; font-size: 19px; line-height: 30px;
  }
  .contact-list li { display: flex; align-items: flex-start; }
  .contact-list svg { width: 18px; height: 18px; margin: 6px 18px 0 0; flex: none; }
  .contact-list .no-icon { margin-left: 36px; }

  /* wordmark */
  .wordmark { display: flex; align-items: center; gap: 10px; color: var(--navy); font-weight: 700; }
  .wordmark__square { background: var(--orange); flex: none; }
  .wordmark--small { font-size: 40px; }
  .wordmark--small .wordmark__square { width: 22px; height: 22px; }
  .wordmark--large { font-size: 96px; }
  .wordmark--large .wordmark__square { width: 50px; height: 50px; }
  .tagline--small { color: var(--orange); font-size: 9.5px; font-weight: 700; }
  .website { color: var(--orange); font-size: 19px; margin-top: 6px; }

  /* brand side */
  .card--brand .brand-stack {
    position: absolute; inset: 0;
    display: flex; flex-direction: column; align-items: center; justify-content: center;
    gap: 14px;
  }
  .tagline--large { color: var(--navy); font-size: 25px; font-weight: 700; }
</style>
</head>
<body>
  <section class="card card--contact">
    <div class="edge-band"></div>
    <div class="brand-column">
      <div class="wordmark wordmark--small"><span class="wordmark__square"></span>Corvana</div>
      <p class="tagline--small">Intelligent annotation solutions for complex data</p>
      <p class="website">Your Website</p>
    </div>
    <div class="info-panel">
      <div class="person">
        <p class="person__name">Your Name</p>
        <p class="person__title">Title</p>
      </div>
      <ul class="contact-list">
        <li>
          <svg viewBox="0 0 24 24" aria-hidden="true"><path fill="#fff" d="M12 2a7 7 0 0 0-7 7c0 5 7 13 7 13s7-8 7-13a7 7 0 0 0-7-7zm0 9.5A2.5 2.5 0 1 1 12 6.5a2.5 2.5 0 0 1 0 5z"/></svg>
          <span>Your City</span>
        </li>
        <li><span class="no-icon">Your State</span></li>
        <li>
          <svg viewBox="0 0 24 24" aria-hidden="true"><rect x="2" y="5" width="20" height="14" fill="#fff"/><path d="M2 5l10 8 10-8" fill="none" stroke="var(--navy)" stroke-width="1.6"/></svg>
          <span>Your Email.com</span>
        </li>
        <li>
          <svg viewBox="0 0 24 24" aria-hidden="true"><rect x="7" y="2" width="10" height="20" rx="1.5" fill="none" stroke="#fff" stroke-width="1.8"/><line x1="10.5" y1="18.5" x2="13.5" y2="18.5" stroke="#fff" stroke-width="1.5"/></svg>
          <span>Your Phone Number</span>
        </li>
      </ul>
    </div>
  </section>

  <section class="card card--brand">
    <div class="brand-stack">
      <div class="wordmark wordmark--large"><span class="wordmark__square"></span>Corvana</div>
      <p class="tagline--large">Intelligent annotation solutions for complex data</p>
    </div>
  </section>
</body>
</html>
```